Tessbury Pure Twist Label

We are looking for a label for our blueberry vodka and lemonade ready-to-drink cocktail. we would like the ingredients (vodka, lemon juice, cane sugar, blueberries) discretely displayed on the label. We would also like 15% alc/vol (30 proof) on the label. The label is for a 12-ounce slim can. We would also like the Surgeon Generals warning ion the label

Target Market(s)

Spike seltzer and ready to drink cocktail drinkers

Font styles to use
Decorative

Requirements
Must have
• Surgeon General warning, 15% alc/vol (30 proof) 12 ounces., Ingredients

```html
<!DOCTYPE html>
<html lang="en">
<head>
<meta charset="utf-8">
<title>Tessbury Pure Twist Label</title>
<link rel="stylesheet" href="https://fonts.googleapis.com/css2?family=IM+Fell+English&family=IM+Fell+English+SC&family=Oswald:wght@500&display=swap">
<style>
  :root {
    --backdrop: #dcdcdc;
    --label-gold: #fcc800;
    --label-gold-deep: #f8bd00;
    --lemon-pale: #fbeea6;
    --lemon-rind: #f6d54a;
    --cream-band: #f6ea9c;
    --cream-band-low: #f9e879;
    --ink: #111111;
  }
  * { margin: 0; padding: 0; box-sizing: border-box; }
  html, body {
    width: 1200px; height: 1200px; overflow: hidden;
    background: radial-gradient(circle at 50% 40%, #ececec, var(--backdrop));
  }
  .label {
    position: absolute; left: 374px; top: 60px;
    width: 452px; height: 1080px;
    box-shadow: 6px 8px 16px rgba(0,0,0,0.3);
    overflow: hidden;
  }
  .label-art { position: absolute; inset: 0; }
  .copy {
    position: absolute; left: 0; width: 100%;
    text-align: center; color: var(--ink);
  }
  .category {
    top: 338px;
    font-family: "IM Fell English SC", serif;
    font-size: 23px; letter-spacing: 0.5px;
  }
  .product-name {
    top: 398px;
    font-family: "IM Fell English SC", serif;
    font-weight: 400; line-height: 0.95;
  }
  .product-name .line-one { display: block; font-size: 74px; letter-spacing: 1px; }
  .product-name .line-two { display: block; font-size: 80px; letter-spacing: 1px; }
  .ingredients {
    top: 578px;
    font-family: "IM Fell English", serif;
    font-size: 23px; line-height: 1.15;
  }
  .strength {
    position: absolute; top: 678px;
    font-family: "Oswald", sans-serif; font-weight: 500;
    font-size: 10px; line-height: 1.5; text-align: center;
    color: var(--ink);
  }
  .strength.proof { left: 58px; }
  .strength.abv { right: 62px; }
  .volume {
    top: 1000px;
    font-family: "IM Fell English", serif;
    font-size: 22px; line-height: 1.05;
  }
  .warning {
    position: absolute; left: 14px; top: 1072px;
    width: 250px;
    transform: rotate(-90deg); transform-origin: 0 0;
    font-family: "Oswald", sans-serif; font-size: 6.5px; line-height: 1.5;
    color: var(--ink);
  }
</style>
</head>
<body>
  <div class="label">
    <svg class="label-art" viewBox="0 0 452 1080" width="452" height="1080">
      <defs>
        <linearGradient id="goldBody" x1="0" y1="0" x2="0" y2="1">
          <stop offset="0" stop-color="var(--label-gold-deep)"/>
          <stop offset="1" stop-color="var(--label-gold)"/>
        </linearGradient>
        <linearGradient id="lemonTop" x1="0" y1="0" x2="0" y2="1">
          <stop offset="0" stop-color="var(--lemon-pale)"/>
          <stop offset="1" stop-color="var(--lemon-rind)"/>
        </linearGradient>
        <linearGradient id="creamBand" x1="0" y1="0" x2="0" y2="1">
          <stop offset="0" stop-color="var(--cream-band)"/>
          <stop offset="1" stop-color="var(--cream-band-low)"/>
        </linearGradient>
      </defs>
      <rect class="gold-body" width="452" height="1080" fill="url(#goldBody)"/>
      <path class="lemon-slices" role="img" aria-label="Illustration of overlapping lemon slices with dripping juice"
        fill="url(#lemonTop)"
        d="M0 0 H452 V232 C430 240 410 236 392 232 C370 244 350 250 330 246 C300 252 270 258 240 254 C215 262 190 270 165 266 C140 276 110 282 85 276 C60 284 30 290 0 282 Z"/>
      <path class="cream-band" fill="url(#creamBand)"
        d="M0 808 C30 800 50 790 70 792 C90 780 110 786 130 790 C150 780 170 770 190 772 C215 768 235 772 250 774 C265 762 280 760 292 756 C310 744 330 742 350 740 C370 738 385 742 395 734 C410 736 430 746 452 742 V1080 H0 Z"/>
    </svg>

    <p class="copy category">Ready~to~Drink Cocktail</p>
    <h1 class="copy product-name">
      <span class="line-one">Lemonade</span>
      <span class="line-two">Cocktail</span>
    </h1>
    <p class="copy ingredients">Vodka, Lemon Juice, Cane Sugar,<br>Blueberries</p>
    <p class="strength proof">30<br>PROOF</p>
    <p class="strength abv">15%<br>ALC/VOL</p>
    <p class="copy volume">12 fl oz<br>(355 ml)</p>
    <p class="warning">WARNING: Smoking Causes Lung Cancer, Heart Disease, Emphysema,<br>and May Complicate Pregnancy.</p>
  </div>
</body>
</html>
```